Book cover for LM

Design cover for a book of gratitude and inspiration.
Book trim size will be 6.5 x 6.5 inches, or 8 x 8 inches, hardcover, 96 pages
Title: Lantern Meadows
Subtitle: A Book of Gratitude and Inspiration
Author: Gus Halverd

```html
<!DOCTYPE html>
<html lang="en">
<head>
<meta charset="utf-8">
<title>Lantern Meadows — Gus Halverd</title>
<link rel="stylesheet" href="https://fonts.googleapis.com/css2?family=Montserrat:wght@500;700&family=Yellowtail&family=Lobster&display=block">
<style>
  :root {
    --sky-top: #3d5c9e;
    --sky-mid: #7d9bc4;
    --haze: #a7a9a0;
    --glow: #f2b23c;
    --glow-deep: #e07a1c;
    --ground: #0b0b0b;
    --ink-light: #ffffff;
    --accent: #f39c1f;
  }
  html, body {
    margin: 0;
    padding: 0;
    width: 1200px;
    height: 1200px;
    overflow: hidden;
    background: var(--ground);
  }
  .cover {
    position: relative;
    width: 1200px;
    height: 1200px;
    overflow: hidden;
  }
  .cover-photo {
    position: absolute;
    inset: 0;
    background:
      radial-gradient(ellipse 240px 150px at 930px 560px, rgba(255, 214, 110, 0.95), rgba(242, 178, 60, 0.6) 45%, rgba(242, 178, 60, 0) 100%),
      radial-gradient(ellipse 650px 190px at 820px 600px, rgba(224, 122, 28, 0.5), rgba(224, 122, 28, 0) 100%),
      linear-gradient(180deg,
        var(--sky-top) 0%,
        #4f70ad 22%,
        var(--sky-mid) 40%,
        var(--haze) 50%,
        #6b5a3e 58%,
        #1c1710 66%,
        var(--ground) 76%,
        var(--ground) 100%);
  }
  .subtitle {
    position: absolute;
    top: 72px;
    left: 0;
    width: 100%;
    margin: 0;
    text-align: center;
    font-family: "Montserrat", sans-serif;
    font-weight: 500;
    font-size: 38px;
    letter-spacing: 1px;
    color: var(--ink-light);
  }
  .title {
    margin: 0;
    font-weight: 400;
  }
  .title-lead {
    position: absolute;
    left: 130px;
    top: 572px;
    font-family: "Montserrat", sans-serif;
    font-weight: 500;
    font-size: 66px;
    letter-spacing: 1px;
    color: var(--ink-light);
    line-height: 1;
  }
  .title-script {
    position: absolute;
    left: 100px;
    width: 1000px;
    top: 690px;
    text-align: center;
    white-space: nowrap;
    font-family: "Yellowtail", "Lobster", cursive;
    font-weight: 400;
    font-size: 270px;
    line-height: 1;
    color: var(--ink-light);
    text-shadow: 8px 8px 0 var(--accent);
  }
  .author {
    position: absolute;
    top: 1030px;
    left: 0;
    width: 100%;
    margin: 0;
    text-align: center;
    padding-left: 60px;
    box-sizing: border-box;
    font-family: "Montserrat", sans-serif;
    font-weight: 700;
    font-size: 50px;
    letter-spacing: 1px;
    color: var(--accent);
  }
</style>
</head>
<body>
  <main class="cover">
    <div class="cover-photo" role="img" aria-label="Photograph of a grass seed head silhouetted against a blue dusk sky with an orange sunset glow over a dark horizon"></div>
    <p class="subtitle">A BOOK OF GRATITUDE AND INSPIRATION</p>
    <h1 class="title">
      <span class="title-lead">LANTERN</span>
      <span class="title-script">Meadows</span>
    </h1>
    <p class="author">GUS HALVERD</p>
  </main>
</body>
</html>
```